Photography Studio Prep Guide Design Needed

I have a prep guide I send to all parents who book a session - It is outdated and ugly. I want a gorgeous, clean, modern upscale look for the brochure I send.

I already have the text and can provide photos for the final design. I want the cover to be clean and upscale and modern, with a happy feel.

Target Market(s)

My clients for an upscale Newborn Photography Studio

Requirements
Must have
• space for my photos, an upscale clean feel
Nice to have
• I love color, but don't want the brochure to look busy. I love cream, white, pale pink.

```html
<!DOCTYPE html>
<html lang="en">
<head>
<meta charset="utf-8">
<title>Newborn Session Prep Guide</title>
<link rel="stylesheet" href="https://fonts.googleapis.com/css2?family=Playfair+Display:ital,wght@0,700;1,400;1,700&family=Josefin+Sans:wght@300;400&family=Great+Vibes&display=swap">
<style>
  :root {
    --backdrop: #ecd8d4;
    --paper: #ffffff;
    --paper-shade: #f4f2f1;
    --blush: #eec4c4;
    --blush-soft: #f3dede;
    --gold: #d8b449;
    --ink: #6f6f6f;
    --ink-dark: #4a4a4a;
    --photo-night: #7c98a6;
    --photo-night-deep: #4d6674;
    --photo-cream: #efe4da;
    --photo-rose: #e6cfc8;
  }
  * { box-sizing: border-box; margin: 0; padding: 0; }
  html, body { width: 1200px; height: 1000px; overflow: hidden; }
  body {
    background: var(--backdrop);
    font-family: "Josefin Sans", sans-serif;
    color: var(--ink);
    position: relative;
  }
  .page {
    position: absolute;
    top: 285px;
    width: 300px;
    height: 430px;
    background: var(--paper);
    box-shadow: 0 6px 18px rgba(120, 80, 80, 0.18);
  }
  .page--photo { left: 60px; padding: 0; }
  .page--welcome { left: 360px; }
  .page--faq { left: 800px; }

  .cover-photo {
    width: 100%;
    height: 100%;
    background: linear-gradient(180deg, var(--photo-night) 0%, #9db2bb 45%, var(--photo-night-deep) 100%);
  }

  .page-title {
    font-family: "Playfair Display", serif;
    font-weight: 700;
    color: var(--blush);
    font-size: 27px;
    line-height: 1;
  }
  .page-subtitle {
    font-weight: 300;
    text-transform: uppercase;
    letter-spacing: 0.6px;
    font-size: 10.5px;
    color: var(--ink-dark);
    margin-top: 4px;
  }
  .section-heading {
    font-family: "Playfair Display", serif;
    font-style: italic;
    font-weight: 700;
    color: var(--gold);
    font-size: 10.5px;
    margin-bottom: 3px;
  }
  .section-body {
    font-size: 5.6px;
    line-height: 1.5;
    text-transform: uppercase;
    letter-spacing: 0.25px;
    color: var(--ink);
  }
  .page-footer {
    position: absolute;
    left: 0; right: 0; bottom: 12px;
    text-align: center;
    font-size: 7px;
    letter-spacing: 1.4px;
    text-transform: uppercase;
    color: var(--ink-dark);
  }

  /* welcome page */
  .welcome-header { position: absolute; left: 20px; top: 30px; right: 20px; }
  .welcome-intro { position: absolute; left: 20px; top: 84px; width: 160px; }
  .instructions { position: absolute; left: 20px; top: 140px; width: 118px; }
  .instruction { margin-bottom: 14px; }
  .photo-column {
    position: absolute;
    left: 150px; top: 92px;
    width: 124px;
    display: flex; flex-direction: column; gap: 6px;
  }
  .photo-tile { width: 100%; }
  .photo-tile--top { height: 68px; background: linear-gradient(135deg, var(--photo-cream), var(--photo-rose)); }
  .photo-tile--bottom { height: 102px; background: linear-gradient(160deg, #f3ede6, #dcd0c5); }
  .tagline-box {
    height: 66px;
    background: var(--blush-soft);
    display: flex; align-items: center; justify-content: center;
    text-align: center;
    font-family: "Great Vibes", cursive;
    font-size: 16px;
    line-height: 1.1;
    color: var(--ink-dark);
    padding: 0 8px;
  }

  /* faq page */
  .faq-header { position: absolute; left: 22px; top: 26px; right: 18px; }
  .faq-header .page-title { font-size: 24px; }
  .faq-list { position: absolute; left: 22px; right: 20px; top: 86px; }
  .faq-item { margin-bottom: 9px; }
  .faq-item .section-heading { font-size: 10px; margin-bottom: 2px; }
</style>
</head>
<body>

  <section class="page page--photo">
    <div class="cover-photo" role="img" aria-label="Newborn baby asleep in a small blue boat prop against a starry night backdrop with a crescent moon"></div>
  </section>

  <section class="page page--welcome">
    <header class="welcome-header">
      <h1 class="page-title">Congratulations</h1>
      <p class="page-subtitle">On expecting your new baby</p>
    </header>

    <div class="welcome-intro">
      <h2 class="section-heading">Parent Instructions &amp; Preparation</h2>
      <p class="section-body">Here are my instructions to ensure a smooth photography session. Please follow them as closely as possible.</p>
    </div>

    <div class="instructions">
      <div class="instruction">
        <h3 class="section-heading">Nursing</h3>
        <p class="section-body">If you are nursing, please avoid spicy foods the day before so baby stays calm and settled.</p>
      </div>
      <div class="instruction">
        <h3 class="section-heading">Feeding</h3>
        <p class="section-body">Feed the baby as much as possible in the hour before your session so they arrive sleepy and content.</p>
      </div>
      <div class="instruction">
        <h3 class="section-heading">Keeping Warm</h3>
        <p class="section-body">Bring a soft blanket and dress baby in layers. The studio is kept warm for comfort.</p>
      </div>
      <div class="instruction">
        <h3 class="section-heading">Pacifier</h3>
        <p class="section-body">Please bring a pacifier. It can be very helpful during a session.</p>
      </div>
    </div>

    <div class="photo-column">
      <div class="photo-tile photo-tile--top" role="img" aria-label="Close-up of a sleeping newborn's face on a cream blanket"></div>
      <div class="tagline-box">capturing life's sweetest moments</div>
      <div class="photo-tile photo-tile--bottom" role="img" aria-label="Newborn wrapped in a chunky knit blanket held in a parent's hands"></div>
    </div>

    <p class="page-footer">Clara Wynne Photography</p>
  </section>

  <section class="page page--faq">
    <header class="faq-header">
      <h1 class="page-title">What You Need To Know</h1>
      <p class="page-subtitle">Before your session</p>
    </header>

    <div class="faq-list">
      <div class="faq-item">
        <h3 class="section-heading">Can I Share My Gallery?</h3>
        <p class="section-body">Yes. Your private gallery link can be shared with family and friends to view and order prints.</p>
      </div>
      <div class="faq-item">
        <h3 class="section-heading">How Can I Download My Photos?</h3>
        <p class="section-body">Use the download button at the top of your gallery to save full resolution files to any device.</p>
      </div>
      <div class="faq-item">
        <h3 class="section-heading">What If My Baby Won't Sleep?</h3>
        <p class="section-body">Interact with baby and keep them awake for two hours beforehand. We never rush, and we pause for cuddles.</p>
      </div>
      <div class="faq-item">
        <h3 class="section-heading">What Poses Will You Do?</h3>
        <p class="section-body">Every pose is chosen for baby's comfort. We work with classic curled, wrapped and parent poses.</p>
      </div>
      <div class="faq-item">
        <h3 class="section-heading">Will My Baby Be Safe?</h3>
        <p class="section-body">Safety comes first. Every pose is spotted by hand and composites are used for any lifted positions.</p>
      </div>
      <div class="faq-item">
        <h3 class="section-heading">What If My Baby Has Acne?</h3>
        <p class="section-body">Newborn acne is very common. Gentle skin retouching is included on every image you receive.</p>
      </div>
      <div class="faq-item">
        <h3 class="section-heading">How Many Props Can I Choose?</h3>
        <p class="section-body">Choose up to three setups from the studio collection. Wraps, hats and blankets are all included.</p>
      </div>
    </div>

    <p class="page-footer">Clara Wynne Photography</p>
  </section>

</body>
</html>
```